St. Bramwell School
St. Bramwell School Fernvale
i have upload design please check it
I would appreciate your feedback on my designs.
Regards
PrimoPixelWorks4
Designers: I have uploaded the logo and pictures to be used in the brochure. The project details are in the brief. Once the design is set, I will work with the designer to add text.
The logo has been uploaded.
where we can find the details of this project...can you upload the details in pdf format or in word format..so that we can start designing it.
tandemvisuals
Philippines

```html
<!DOCTYPE html>
<html lang="en">
<head>
<meta charset="utf-8">
<title>St. Bramwell School Brochure</title>
<link href="https://fonts.googleapis.com/css2?family=Arimo:ital,wght@0,400;0,700;1,400&display=swap" rel="stylesheet">
<style>
  :root {
    --canvas: #f1f1f1;
    --paper: #ffffff;
    --ink: #2b2b2b;
    --heading: #1d3f78;
    --navy: #1f4f9c;
    --navy-deep: #173e80;
    --gold: #d9a421;
    --building-a: #d8cfc3;
    --building-b: #a8957f;
    --class-a: #7a5d42;
    --class-b: #c9a77e;
    --teacher-a: #d6d2cc;
    --teacher-b: #8c8478;
    --field-a: #4f8232;
    --field-b: #9cbf6b;
    --map-a: #eae3cf;
    --map-b: #c2d2aa;
  }
  * { box-sizing: border-box; margin: 0; padding: 0; }
  html, body {
    width: 1200px; height: 842px; overflow: hidden;
    background: var(--canvas);
    font-family: "Arimo", Arial, sans-serif;
    color: var(--ink);
  }
  .spread { position: relative; width: 1200px; height: 842px; }
  .page {
    position: absolute; top: 8px; width: 584px; height: 826px;
    background: var(--paper);
    box-shadow: 0 0 4px rgba(0,0,0,.15);
    overflow: hidden;
  }
  .page--inside { left: 10px; }
  .page--outside { left: 606px; }
  .block { position: absolute; overflow: hidden; }
  p { font-size: 11.8px; line-height: 1.3; text-indent: 16px; }
  h2 {
    font-size: 12.5px; font-weight: 700; color: var(--heading);
    text-align: center; margin-bottom: 2px;
  }
  .justify p { text-align: justify; }
  .lead p { font-size: 12.6px; font-style: italic; line-height: 1.4; }
  .photo { position: absolute; }
  .photo--building { left: 14px; top: 10px; width: 556px; height: 232px;
    background: linear-gradient(100deg, #f3efe8, var(--building-a) 45%, var(--building-b) 75%, #efe9e0); }
  .photo--classroom { left: 304px; top: 318px; width: 268px; height: 184px;
    background: linear-gradient(135deg, var(--class-b), var(--class-a)); }
  .photo--teacher { left: 16px; top: 478px; width: 270px; height: 160px;
    background: linear-gradient(120deg, #ece9e4, var(--teacher-a) 40%, var(--teacher-b)); }
  .photo--field { left: 14px; top: 212px; width: 270px; height: 276px;
    background: linear-gradient(180deg, #6d8d5c, var(--field-a) 40%, var(--field-b)); }
  .photo--map { left: 302px; top: 402px; width: 268px; height: 290px;
    background: linear-gradient(135deg, var(--map-a), var(--map-b)); }
  .school-name {
    position: absolute; left: 418px; top: 16px; width: 156px;
    padding: 8px 10px; background: var(--paper);
    display: flex; align-items: center; gap: 8px;
    font-size: 22px; font-weight: 700; color: var(--heading); line-height: 1.05;
  }
  .school-name__mark {
    flex: none; width: 16px; height: 16px; border-radius: 50%;
    background: var(--navy);
  }
  .bullets { list-style: none; }
  .bullets li {
    font-size: 11.8px; line-height: 1.4; padding-left: 22px; position: relative;
  }
  .bullets li::before {
    content: ""; position: absolute; left: 4px; top: 5px;
    width: 7px; height: 7px; border-radius: 50%; background: var(--ink);
  }
  .footer { position: absolute; left: 0; bottom: 0; width: 100%; height: 70px;
    background: linear-gradient(180deg, var(--navy), var(--navy-deep));
    border-top: 4px solid var(--gold); color: #fff; padding: 10px 18px 0; }
  .footer__title { font-size: 15px; font-weight: 700; margin-bottom: 3px; }
  .footer__line { font-size: 11.5px; }
</style>
</head>
<body>
<main class="spread">

  <section class="page page--inside">
    <div class="photo photo--building" role="img" aria-label="Sketch illustration of the school church building"></div>
    <div class="school-name"><span class="school-name__mark"></span><span>St. Bramwell School</span></div>

    <div class="block justify" style="left:16px; top:252px; width:270px; height:222px;">
      <h2>Mission Statement</h2>
      <p>Sed ut perspiciatis unde omnis iste natus error sit voluptatem accusantium doloremque laudantium, totam rem aperiam, eaque ipsa quae ab illo inventore veritatis et quasi architecto beatae vitae dicta sunt explicabo.</p>
      <p>At vero eos et accusamus et iusto odio dignissimos ducimus qui blanditiis praesentium voluptatum deleniti atque corrupti quos dolores et quas molestias excepturi sint occaecati cupiditate non provident, similique sunt in culpa qui officia deserunt mollitia animi, id est laborum et dolorum fuga.</p>
    </div>

    <div class="photo photo--teacher" role="img" aria-label="Photo of a teacher at the classroom whiteboard"></div>

    <div class="block justify" style="left:16px; top:648px; width:270px; height:100px;">
      <p>Et harum quidem rerum facilis est et expedita distinctio. Nam libero tempore, cum soluta nobis est eligendi optio cumque nihil impedit.</p>
    </div>

    <div class="block justify" style="left:304px; top:254px; width:268px; height:60px;">
      <p style="text-indent:0">impedit quo minus id quod maxime placeat facere possimus, omnis voluptas assumenda est, omnis dolor repellendus.</p>
    </div>

    <div class="photo photo--classroom" role="img" aria-label="Photo of pupils working in a classroom"></div>

    <ul class="bullets block" style="left:304px; top:514px; width:268px; height:160px;">
      <li>Nemo enim ipsam</li>
      <li>voluptatem quia</li>
      <li>voluptas sit aspernatur</li>
      <li>aut odit aut fugit</li>
      <li>sed quia consequuntur</li>
      <li>magni dolores eos</li>
      <li>qui ratione voluptatem</li>
      <li>sequi nesciunt</li>
      <li>Neque porro quisquam</li>
    </ul>

    <footer class="footer">
      <div class="footer__title">Lorem ipsum dolor sit amet,</div>
      <div class="footer__line">consectetur adipisicing elit, sed do eiusmod tempor incididunt ut labore et dolore magna aliqua.</div>
    </footer>
  </section>

  <section class="page page--outside">
    <div class="block justify lead" style="left:16px; top:12px; width:552px; height:84px;">
      <p>At vero eos et accusamus et iusto odio dignissimos ducimus qui blanditiis praesentium voluptatum deleniti atque corrupti quos dolores et quas molestias excepturi sint occaecati cupiditate non provident, similique sunt in culpa qui officia deserunt mollitia animi, id est laborum et dolorum fuga.</p>
    </div>

    <div class="block justify" style="left:14px; top:100px; width:270px; height:108px;">
      <h2>Et harum quidem</h2>
      <p>Sed ut perspiciatis unde omnis iste natus error sit voluptatem accusantium doloremque laudantium, totam rem aperiam, eaque ipsa quae ab illo inventore veritatis et quasi architecto beatae vitae dicta sunt explicabo.</p>
    </div>

    <div class="photo photo--field" role="img" aria-label="Photo of children playing football on the school field"></div>

    <div class="block justify" style="left:14px; top:496px; width:270px; height:254px;">
      <p>Nemo enim ipsam voluptatem quia voluptas sit aspernatur aut odit aut fugit, sed quia consequuntur magni dolores eos qui ratione voluptatem sequi nesciunt. Neque porro quisquam est, qui dolorem ipsum quia dolor sit amet, consectetur, adipisci velit, sed quia non numquam eius modi tempora incidunt ut labore et dolore magnam aliquam quaerat voluptatem. Ut enim ad minima veniam, quis nostrum exercitationem ullam corporis suscipit laboriosam, nisi ut aliquid ex ea commodi consequatur? Quis autem vel eum iure reprehenderit qui in ea.</p>
    </div>

    <div class="block justify" style="left:302px; top:100px; width:268px; height:296px;">
      <h2>At vero eos</h2>
      <p>At vero eos et accusamus et iusto odio dignissimos ducimus qui blanditiis praesentium voluptatum deleniti atque corrupti quos dolores et quas molestias excepturi sint occaecati cupiditate non provident, similique sunt in culpa qui officia deserunt mollitia animi, id est laborum et dolorum fuga.</p>
      <h2 style="margin-top:6px">At vero eos</h2>
      <p>Et harum quidem rerum facilis est et expedita distinctio. Nam libero tempore, cum soluta nobis est eligendi optio cumque nihil impedit quo minus id quod maxime placeat facere possimus, omnis voluptas assumenda est, omnis dolor repellendus. Neque porro quisquam est, qui dolorem ipsum quia dolor sit amet, consectetur.</p>
    </div>

    <div class="photo photo--map" role="img" aria-label="Street map showing the school location"></div>

    <footer class="footer">
      <div class="footer__title">Lorem ipsum dolor sit amet,</div>
      <div class="footer__line">consectetur adipisicing elit, sed do eiusmod tempor incididunt ut labore et dolore magna aliqua.</div>
    </footer>
  </section>

</main>
</body>
</html>
```